Banner to Drive Business Users to Sign Up

Hi,

Banner One (static banner)
I would like you to redesign this page with a single banner of dimensions 600X400:

http://www.hamletsnap.example.au/Business-Listing.html

The text in the banner should be something like:

Have a Local Business? Advertise directly to people in Your Suburb
List a Local Business, attract Local Customers
List Today and Get a Free Business Page
Upload Pictures To Promote Your Business
Maintain a Blog to Promote Your Business

Of course modifications on this text is allowed.

The site is an Australian site, listing local news and stories from around Australia. The site is broken down into individual suburbs that allow business user to list there business. This allows business to target a specific audience within their local area. Access to screenshots and other images can be provided upon request.
The aim is to create a professional banner that encourages people to sign up. Currently the service is free for 2 months and then $22/year. Any other questions can be answered.

The current page describes the service but is poorly designed.
Banner 2 (static Banner)
If you go to this page:

http://www.hamletsnap.example.au/

The banner on the right "List your business" needs to be redesigned to complement Banner 1 (can just be scaled down) as above and should draw business users to sign up. Dimensions should be 468 X 60 (which I know is bigger then current banner).

Looking forward to Your Designs

Target Market(s)

Small Business Owners, Australians

Industry/Entity Type

Business

Requirements
Should not have
• Tackiness, or poor graphics

```html
<!DOCTYPE html>
<html lang="en">
<head>
<meta charset="utf-8">
<title>Hamletsnap – List a Local Business</title>
<link rel="stylesheet" href="https://fonts.googleapis.com/css2?family=Open+Sans:wght@600;700;800&family=Arimo:wght@400&display=swap">
<style>
  :root {
    --bg-top: #e6f2f8;
    --bg-bottom: #fbfdfe;
    --ink: #111111;
    --brand-blue: #1e90e0;
    --cta-top: #ffd45a;
    --cta-mid: #ffab1f;
    --cta-bottom: #f07f00;
    --cta-edge: #e0900f;
    --cta-text: #ffffff;
    --note: #222222;
    --photo-a: #d7e8f2;
    --photo-b: #eef5f9;
    --photo-c: #c9dcea;
  }
  html, body {
    margin: 0;
    padding: 0;
    width: 1200px;
    height: 800px;
    overflow: hidden;
  }
  .banner {
    position: relative;
    width: 1200px;
    height: 800px;
    overflow: hidden;
    background: linear-gradient(180deg, var(--bg-top) 0%, #f1f8fb 60%, var(--bg-bottom) 100%);
    font-family: "Open Sans", Arial, sans-serif;
  }
  .banner__photo {
    position: absolute;
    left: 0;
    top: 0;
    width: 600px;
    height: 800px;
    background:
      radial-gradient(ellipse 220px 300px at 210px 330px, var(--photo-c) 0%, rgba(201,220,234,0) 100%),
      linear-gradient(90deg, var(--photo-a) 0%, var(--photo-b) 70%, rgba(238,245,249,0) 100%);
  }
  .headline {
    position: absolute;
    left: 428px;
    margin: 0;
    line-height: 1;
    white-space: nowrap;
  }
  .headline--lead {
    font-weight: 800;
    font-size: 60px;
    letter-spacing: 3px;
    color: var(--ink);
  }
  .headline--key {
    font-weight: 600;
    font-size: 120px;
    letter-spacing: 4px;
    color: var(--brand-blue);
  }
  .headline--list { top: 76px; }
  .headline--business { top: 140px; }
  .headline--attract { top: 306px; }
  .headline--customers { top: 370px; }

  .cta {
    position: absolute;
    left: 536px;
    top: 594px;
    width: 440px;
    height: 102px;
    box-sizing: border-box;
    border: 2px solid var(--cta-edge);
    border-radius: 8px;
    background: linear-gradient(180deg, var(--cta-top) 0%, var(--cta-mid) 48%, var(--cta-bottom) 100%);
    box-shadow: 0 10px 14px rgba(0, 40, 80, 0.18);
    display: flex;
    align-items: center;
    justify-content: center;
    color: var(--cta-text);
    font-weight: 700;
    font-size: 36px;
    letter-spacing: 1px;
    text-decoration: none;
    text-shadow: 0 2px 2px rgba(120, 60, 0, 0.45);
  }
  .note {
    position: absolute;
    left: 16px;
    top: 738px;
    margin: 0;
    font-family: "Arimo", Arial, sans-serif;
    font-size: 36px;
    color: var(--note);
    line-height: 1.1;
  }
</style>
</head>
<body>
  <main class="banner">
    <div class="banner__photo" role="img" aria-label="Photo of a business owner working on a laptop at a bright desk"></div>

    <p class="headline headline--lead headline--list">LIST A LOCAL</p>
    <p class="headline headline--key headline--business">BUSINESS</p>
    <p class="headline headline--lead headline--attract">ATTRACT LOCAL</p>
    <p class="headline headline--key headline--customers">CUSTOMERS</p>

    <a class="cta" href="http://www.hamletsnap.example.au/Business-Listing.html">SIGN UP NOW</a>

    <p class="note">Try It Now For Free</p>
  </main>
</body>
</html>
```